We have a small 501C Non-Profit, called Youthful Hands. The non-profit was started by my son and his friends during the Gulf Oil Spill. We would like to update the website that currently sits on Namehaven.com. I'm not sure how we transfer over the domain or get them to host it with your new design. I've attached a link of the old site that we developed. We are open to any ideas regarding hosting.

We would basically like a look that is youth (teen, college age) oriented that will drive teens and donors to the site. Our goal is to get onto Brightwall Drives, get grants and make major donations with little to no administration expense. We will get sponsors to pay for the administration costs. So we will be looking for sponsors to support the overhead and 100% of donor money will go to causes important to teens.

http://www.youthfulhands.org

Target Market(s)

Teenagers and Individual Sponsors. Adults that want to help teens with an important cause.

Industry/Entity Type

Non-Profit

Requirements
Must have
• We are very open to ideas. It would be good to have a:

Home-with Mission Statement and Photos or Graphics
Donate-100% of Donations Go To Causes (with Coinpost Link)
Become A Sponsor-Insert Contact Information In This Section.
How It All Got Started -with info, articles, events, video, etc. from Gulf Oil Spill, Our Founder photo.
Contact-Change phone number to 555-318-2704. Keep e-mail and mailing the same.

You can use some existing photos from current site if you would like. All the Recent Event Photos, Founder Photo, 3 people holding check photo were all taken by me so there are no rights issues with those.

YH Mission Statement:

To demonstrate to the world that Youthful Hands about the environment, each other and world peace through fund raising and other philanthropic efforts.
Nice to have
• Youthful Hands Logo If Possible

Photo of 3 people, holding check, from existing home page in new History Section.

Kindly Paws League Story and Logo in History Section

WRT Video in History Section

Helpx9
http://www.helpx9.example/causes/teenager-starts-non-profit-to-raise-money-for-animals-victims-of-gulf-oil-spill.html
Should not have
• Delete Blog Section
Delete Founder Section
Delete Recent Events
Delete How To Get Involved

```html
<!DOCTYPE html>
<html lang="en">
<head>
<meta charset="utf-8">
<title>Youthful Hands</title>
<link rel="stylesheet" href="https://fonts.googleapis.com/css2?family=Gilda+Display&family=Questrial&family=Poppins:ital,wght@1,300&family=Mulish:wght@700;800&family=Open+Sans:ital,wght@0,400;1,400;1,600;1,700&display=swap">
<style>
:root{
  --navy:#2f5597;
  --navy-deep:#264a86;
  --contact-blue:#0f4079;
  --band-blue:#8196c5;
  --social-blue:#3d5a99;
  --mission-blue:#3a5a8f;
  --tab-grey:#e2e2e2;
  --ink:#1e1e1e;
  --rule:#9a9a9a;
  --footer-grey:#555558;
  --white:#ffffff;
}
*{margin:0;padding:0;box-sizing:border-box}
html,body{width:1200px;height:741px;overflow:hidden;background:var(--white)}
.page{position:relative;width:1200px;height:741px}
.header-shape{position:absolute;left:120px;top:18px}
.brand-name{position:absolute;left:122px;top:35px;font-family:"Gilda Display",serif;font-size:34px;line-height:44px;color:var(--ink);letter-spacing:.3px;white-space:nowrap}
.brand-dot{position:absolute;left:383px;top:28px;width:57px;height:57px;border-radius:50%;background:var(--navy)}
.nav{position:absolute;left:494px;top:58px;width:570px;display:flex;align-items:center;justify-content:space-between;font-family:"Mulish",sans-serif;font-weight:800;font-size:13.5px;line-height:18px;color:var(--white);white-space:nowrap}
.nav a{color:var(--white);text-decoration:none}
.nav .sep{font-weight:700}
.nav .current{border-bottom:3px solid rgba(255,255,255,.45)}
.hero{position:absolute;left:120px;top:107px;width:960px;height:198px;
  background:linear-gradient(90deg,#6f7f88 0%,#a9a49a 30%,#7a9aa3 55%,#8fa7a9 75%,#6d7a6c 100%);
  box-shadow:0 6px 6px -2px rgba(0,0,0,.25)}
.globe-art{position:absolute;left:120px;top:318px;width:80px;height:82px;border-radius:50%;
  background:radial-gradient(circle at 35% 30%,#e6f4ff 0%,#5bb0ef 35%,#1d6fc0 70%,#0c3f7c 100%)}
.mission-title{position:absolute;left:0;width:1200px;top:318px;text-align:center;font-family:"Poppins",sans-serif;font-style:italic;font-weight:300;font-size:44px;line-height:56px;color:var(--mission-blue)}
.mission-rule{position:absolute;left:200px;top:382px;width:880px;height:1px;background:var(--rule)}
.mission-text{position:absolute;left:120px;width:960px;top:398px;text-align:center;font-family:"Open Sans",sans-serif;font-style:italic;font-weight:700;font-size:18.8px;line-height:26px;color:var(--ink);white-space:nowrap}
.cause-band{position:absolute;left:120px;top:437px;width:960px;height:63px;background:var(--band-blue)}
.cause-band-text{position:absolute;left:22px;top:13px;font-family:"Questrial",sans-serif;font-size:31px;line-height:38px;color:var(--white);text-shadow:1px 1px 2px rgba(0,0,0,.3);white-space:nowrap}
.social{position:absolute;right:0;top:0;width:165px;height:63px;background:var(--social-blue);display:flex;align-items:center;justify-content:center;font-family:"Questrial",sans-serif;font-size:28px;color:var(--white)}
.causes{position:absolute;left:120px;top:500px;width:960px;display:flex;gap:4px}
.cause-tab{flex:1;height:35px;background:var(--tab-grey);border-radius:0 0 10px 10px;font-family:"Questrial",sans-serif;font-size:18.5px;color:var(--ink);text-align:center;line-height:36px}
.sponsor-bar{position:absolute;left:120px;top:558px;width:960px;height:52px;border-radius:13px;background:linear-gradient(#6b6b6b,#1c1c1c 55%,#2d2d2d)}
.sponsor-label{position:absolute;left:22px;top:13px;font-family:"Open Sans",sans-serif;font-style:italic;font-weight:700;font-size:19.5px;line-height:27px;color:var(--white);white-space:nowrap}
.sponsor-input{position:absolute;left:250px;top:11px;width:700px;height:31px;border-radius:9px;background:linear-gradient(#c9c9c9,#eeeeee);padding-left:22px;font-family:"Questrial",sans-serif;font-style:italic;font-size:19px;color:#8d8d8d;line-height:31px}
.sponsor-submit{position:absolute;left:773px;top:10px;width:175px;height:33px;border-radius:8px;background:linear-gradient(#8aa6e0,#2a58a6 45%,#123f82);font-family:"Mulish",sans-serif;font-weight:800;font-size:17px;color:var(--white);text-align:center;line-height:31px}
.contact{position:absolute;left:301px;top:610px;width:620px;height:96px;background:var(--contact-blue);border-radius:0 0 8px 8px;padding-top:13px;text-align:center;font-family:"Questrial",sans-serif;font-style:italic;font-size:19.5px;line-height:23px;color:var(--white);white-space:nowrap}
.footer{position:absolute;left:120px;top:706px}
.copyright{position:absolute;right:126px;top:713px;font-family:"Open Sans",sans-serif;font-size:10.5px;line-height:14px;color:var(--white);white-space:nowrap}
</style>
</head>
<body>
<div class="page">
  <svg class="header-shape" width="960" height="88" viewBox="0 0 960 88" aria-hidden="true">
    <defs>
      <linearGradient id="navFill" x1="0" y1="0" x2="0" y2="1">
        <stop offset="0" stop-color="#4b73b8"/>
        <stop offset="1" stop-color="#27498a"/>
      </linearGradient>
    </defs>
    <polygon points="382,0 960,0 960,88 0,88 0,75 316,75" fill="url(#navFill)"/>
  </svg>

  <span class="brand-name">Youthful Hands</span>
  <span class="brand-dot"></span>

  <nav class="nav">
    <a class="current" href="#">HOME</a><span class="sep">I</span>
    <a href="#">DONATE</a><span class="sep">I</span>
    <a href="#">BECOME A SPONSOR</a><span class="sep">I</span>
    <a href="#">HISTORY</a><span class="sep">I</span>
    <a href="#">NEWS</a><span class="sep">I</span>
    <a href="#">CONTACT</a>
  </nav>

  <div class="hero" role="img" aria-label="Photo strip: a volunteer at a laptop, three men holding a donation check, and a group of teenagers smiling by the water"></div>

  <div class="globe-art" role="img" aria-label="Glossy blue globe illustration"></div>
  <h1 class="mission-title">OUR MISSION</h1>
  <div class="mission-rule"></div>
  <p class="mission-text">Support each other, the environment and the poor, through fund raising and other philanthropic efforts.</p>

  <div class="cause-band">
    <span class="cause-band-text">HELPING OTHERS AROUND THE WORLD &nbsp;I&nbsp; Find us on :</span>
    <div class="social">brightwall</div>
  </div>

  <div class="causes">
    <div class="cause-tab">Hunger</div>
    <div class="cause-tab">Disaster Relief</div>
    <div class="cause-tab">Water</div>
    <div class="cause-tab">Medical</div>
    <div class="cause-tab">Environment</div>
  </div>

  <div class="sponsor-bar">
    <span class="sponsor-label">BECOME A SPONSOR :</span>
    <div class="sponsor-input">Enter your Email Address...</div>
    <div class="sponsor-submit">Submit</div>
  </div>

  <address class="contact">
    Youthful Hands Corp. 48 Dune Lane, Bayview, NJ 08000<br>
    By Phone: 555-318-2704<br>
    customerservice@youthfulhands.org
  </address>

  <svg class="footer" width="960" height="28" viewBox="0 0 960 28" aria-hidden="true">
    <rect x="0" y="0" width="320" height="4" fill="#555558"/>
    <polygon points="315,4 960,4 960,27 385,27" fill="#555558"/>
  </svg>
  <span class="copyright">Copyright © 2012 YouthfulHands. All Rights Reserved</span>
</div>
</body>
</html>
```